Timid Kitten Clinic Business Card Design

I need a business card designed for my cat only veterinary clinic. I will upload the logo that I would like included on the card. Please include:
Business Name: The Timid Kitten Clinic
Address: 4827 W. 39th Ln, Scottsdale, AZ 85317
Phone #: 480-555-6314
Website URL: www.timidkittenvet.example
And the Doctors Name: Marla Quint, DVM

```html
<!DOCTYPE html>
<html lang="en">
<head>
<meta charset="utf-8">
<title>The Timid Kitten Clinic – Business Card</title>
<link href="https://fonts.googleapis.com/css2?family=Quicksand:wght@500;600&family=Montserrat:wght@400;600&display=swap" rel="stylesheet">
<style>
  :root {
    --backdrop: #8a8a88;
    --card: #ffffff;
    --card-edge: #3f6ea8;
    --ink: #1c1c1c;
    --text-grey: #5a5a5a;
    --accent-blue: #4a80c4;
    --accent-pink: #c23f7c;
    --mark: #2a2236;
    --doodle-wash: #eef1f6;
    --photo-warm: #b49686;
    --photo-rose: #d9aab4;
    --photo-dark: #4b3a3a;
  }
  * { box-sizing: border-box; margin: 0; padding: 0; }
  html, body { width: 1200px; height: 801px; overflow: hidden; }
  body {
    background: var(--backdrop);
    font-family: "Montserrat", sans-serif;
    position: relative;
  }
  .card {
    position: absolute;
    width: 540px;
    height: 309px;
    background: var(--card);
    border-bottom: 3px solid var(--card-edge);
    border-left: 2px solid var(--card-edge);
    overflow: hidden;
    box-shadow: 0 10px 24px rgba(0,0,0,0.25);
  }
  .card--front { left: 40px; top: 246px; }
  .card--back { left: 620px; top: 246px; }

  /* front */
  .front__photo {
    position: absolute;
    right: 0; top: 0;
    width: 62%;
    height: 100%;
    background:
      linear-gradient(90deg, #ffffff 0%, rgba(255,255,255,0.6) 25%, rgba(255,255,255,0) 55%),
      radial-gradient(ellipse at 62% 45%, var(--photo-warm) 0%, var(--photo-dark) 40%, var(--photo-rose) 75%, #f1dfe3 100%);
  }
  .brand {
    display: flex;
    align-items: center;
    gap: 12px;
  }
  .brand__dot {
    flex: none;
    border-radius: 50%;
    background: var(--mark);
  }
  .brand__name {
    font-family: "Quicksand", sans-serif;
    font-weight: 600;
    color: var(--ink);
    line-height: 1.02;
  }
  .front__brand { position: absolute; left: 26px; top: 34px; }
  .front__brand .brand__dot { width: 82px; height: 82px; }
  .front__brand .brand__name { font-size: 22px; }

  .doctor {
    position: absolute;
    left: 28px; top: 150px;
    font-weight: 600;
    font-size: 17px;
    color: var(--accent-blue);
  }
  .address {
    position: absolute;
    left: 28px; top: 184px;
    font-size: 12.5px;
    line-height: 1.45;
    color: var(--text-grey);
  }
  .contact {
    position: absolute;
    left: 28px; top: 232px;
    list-style: none;
    font-size: 12.5px;
    line-height: 1.55;
    color: var(--text-grey);
  }
  .contact li { display: flex; align-items: center; gap: 7px; }
  .contact svg { width: 11px; height: 11px; fill: none; stroke: var(--accent-pink); stroke-width: 2; }

  /* back */
  .back__pattern {
    position: absolute;
    inset: 0;
    background: var(--doodle-wash);
  }
  .back__brand {
    position: absolute;
    left: 50%; top: 50%;
    transform: translate(-50%, -50%);
    gap: 16px;
  }
  .back__brand .brand__dot { width: 120px; height: 120px; }
  .back__brand .brand__name { font-size: 34px; white-space: nowrap; }
</style>
</head>
<body>

  <section class="card card--front" aria-label="Business card front">
    <div class="front__photo" role="img" aria-label="Soft-focus photo of a fluffy long-haired cat gazing out a sunlit window"></div>

    <div class="brand front__brand">
      <span class="brand__dot"></span>
      <p class="brand__name">The Timid<br>Kitten Clinic</p>
    </div>

    <h1 class="doctor">Marla Quint, DVM</h1>
    <p class="address">4827 W. 39th Ln<br>Scottsdale, AZ 85317</p>
    <ul class="contact">
      <li>
        <svg viewBox="0 0 24 24" aria-hidden="true"><path d="M5 3h4l2 5-3 2a12 12 0 0 0 6 6l2-3 5 2v4a2 2 0 0 1-2 2A18 18 0 0 1 3 5a2 2 0 0 1 2-2z"/></svg>
        480-555-6314
      </li>
      <li>
        <svg viewBox="0 0 24 24" aria-hidden="true"><circle cx="12" cy="12" r="10"/><path d="M2 12h20M12 2a15 15 0 0 1 0 20M12 2a15 15 0 0 0 0 20"/></svg>
        www.timidkittenvet.example
      </li>
    </ul>
  </section>

  <section class="card card--back" aria-label="Business card back">
    <div class="back__pattern" role="img" aria-label="Faint line-drawn pattern of veterinary doodles: pets, paw prints, medicine and tools"></div>
    <div class="brand back__brand">
      <span class="brand__dot"></span>
      <p class="brand__name">The Timid<br>Kitten Clinic</p>
    </div>
  </section>

</body>
</html>
```